Updated flyer

we are a defence industry trainer and we are updating a course that has been running for a few years, so want a new look flyer. Please note that the flyer is A4 and we would like people to fill in the document online. Please add a tickbox for SME's free and add a call out box saying the course is NEW & UPDATED.

Industry/Entity Type

Defence

Font styles to use
Sans Serif
Other font styles liked:
• AVENIR

Colors
3176b5
01a88e
9bcb3b
fbed22
f37022

```html
<!DOCTYPE html>
<html lang="en">
<head>
<meta charset="utf-8">
<title>Defence, ITAR &amp; EAR Training Controls – Course Flyer</title>
<link rel="stylesheet" href="https://fonts.googleapis.com/css2?family=Oswald:wght@500;600&family=Nunito+Sans:wght@400;700;800&family=PT+Sans:wght@400;700&display=swap">
<style>
  :root {
    --brand-blue: #3176b5;
    --brand-teal: #01a88e;
    --brand-lime: #9bcb3b;
    --brand-yellow: #fbed22;
    --brand-orange: #f37022;
    --green-bright: #8cc63f;
    --green-dark: #2f6e34;
    --green-footer: #3d6b38;
    --cyan: #27a9e1;
    --ink: #1d1d1b;
    --white: #ffffff;
    --shadow: #4a4a4a;
  }
  html, body {
    margin: 0;
    padding: 0;
    width: 848px;
    height: 1200px;
    overflow: hidden;
    background: var(--white);
  }
  .flyer {
    position: relative;
    width: 848px;
    height: 1200px;
    overflow: hidden;
    background: var(--white);
    font-family: "PT Sans", Arial, sans-serif;
    color: var(--ink);
  }

  /* Hero */
  .hero {
    position: absolute;
    left: 0; top: 0;
    width: 848px; height: 556px;
    background: var(--green-bright);
  }
  .hero-globe {
    position: absolute;
    left: 250px; top: 0;
    width: 600px; height: 556px;
    background: radial-gradient(ellipse 60% 55% at 55% 45%, rgba(120,140,110,0.55), rgba(166,209,106,0.25) 60%, rgba(140,198,63,0) 80%);
  }
  .hero-sweep {
    position: absolute;
    left: 0; top: 0;
  }
  .brand {
    position: absolute;
    left: 20px; top: 38px;
    display: flex;
    align-items: center;
    gap: 22px;
  }
  .brand-dot {
    width: 120px; height: 120px;
    border-radius: 50%;
    background: var(--green-dark);
  }
  .brand-name {
    font-family: "Nunito Sans", Arial, sans-serif;
    font-weight: 700;
    font-size: 30px;
    line-height: 34px;
    color: var(--green-dark);
  }

  .badge {
    position: absolute;
    left: 689px; top: 224px;
    width: 136px; height: 136px;
    border-radius: 50%;
    background: var(--white);
    border: 5px solid var(--green-dark);
    box-sizing: border-box;
    display: flex;
    flex-direction: column;
    align-items: center;
    justify-content: center;
    font-family: "Oswald", Arial, sans-serif;
    font-weight: 500;
    font-size: 28px;
    line-height: 40px;
    color: var(--green-dark);
  }

  .headline {
    position: absolute;
    right: 22px; top: 380px;
    margin: 0;
    text-align: right;
    font-family: "Oswald", Arial, sans-serif;
    font-weight: 600;
    font-size: 58px;
    line-height: 60px;
    letter-spacing: -1px;
    color: var(--white);
    text-shadow: 3px 3px 0 var(--shadow);
    transform: scaleX(0.8);
    transform-origin: right top;
  }
  .headline span {
    display: block;
    white-space: nowrap;
  }

  /* Schedule */
  .schedule {
    position: absolute;
    left: 110px; top: 588px;
    width: 610px; height: 190px;
    border-radius: 14px;
    background: var(--brand-lime);
  }
  .schedule-divider {
    position: absolute;
    left: 295px; top: 30px;
    width: 2px; height: 132px;
    background: var(--white);
  }
  .schedule-row {
    position: absolute;
    left: 90px;
    display: flex;
    font-family: "Nunito Sans", Arial, sans-serif;
    font-size: 21px;
    letter-spacing: 1.5px;
    color: var(--white);
  }
  .schedule-city { width: 270px; }

  /* Body */
  .intro {
    position: absolute;
    left: 27px; top: 796px;
    width: 795px;
    font-size: 18px;
    line-height: 24px;
    text-align: justify;
  }
  .intro p { margin: 0 0 11px; }
  .intro strong { color: var(--green-dark); }

  .price, .sme-note, .subsidy-note {
    position: absolute;
    left: 0;
    width: 848px;
    margin: 0;
    text-align: center;
  }
  .price {
    top: 985px;
    font-family: "Nunito Sans", Arial, sans-serif;
    font-weight: 800;
    font-size: 24px;
    letter-spacing: 1.5px;
    color: var(--cyan);
  }
  .price small { font-size: 15px; letter-spacing: 1px; }

  .sme-note {
    top: 1052px;
    font-family: "Nunito Sans", Arial, sans-serif;
    font-size: 25px;
    line-height: 34px;
    letter-spacing: 1.6px;
    color: var(--green-dark);
    display: flex;
    justify-content: center;
    align-items: center;
    gap: 12px;
    top: 1053px;
  }
  .sme-note { top: 1052px; }
  .sme-tick {
    appearance: none;
    -webkit-appearance: none;
    width: 22px; height: 22px;
    margin: 0;
    border: 2px solid var(--green-dark);
    border-radius: 3px;
    background: var(--white);
  }
  .sme-tick:checked { background: var(--green-dark); }

  .subsidy-note {
    top: 1097px;
    font-family: "Nunito Sans", Arial, sans-serif;
    font-size: 24px;
    letter-spacing: 1.6px;
    color: var(--ink);
  }

  .footer {
    position: absolute;
    left: 0; top: 1150px;
    width: 848px; height: 50px;
    background: var(--green-footer);
    display: flex;
    align-items: center;
    justify-content: center;
    font-family: "Nunito Sans", Arial, sans-serif;
    font-weight: 700;
    font-size: 18px;
    letter-spacing: 0.6px;
    color: var(--white);
  }
</style>
</head>
<body>
<main class="flyer">
  <section class="hero">
    <div class="hero-globe" role="img" aria-label="Faint globe with swirling ribbons decoration"></div>
    <svg class="hero-sweep" width="848" height="260" viewBox="0 0 848 260" aria-hidden="true">
      <path d="M0 0 H512 C480 130 300 205 0 240 Z" fill="#5f7f55" opacity="0.45"/>
      <path d="M0 0 H505 C470 120 300 198 0 232 Z" fill="#ffffff"/>
    </svg>
    <div class="brand">
      <div class="brand-dot"></div>
      <div class="brand-name">Northline<br>Trade<br>Compliance</div>
    </div>
    <div class="badge"><span>NEW</span><span>UPDATED</span></div>
    <h1 class="headline">
      <span>DEFENCE, ITAR &amp; EAR TRAINING CONTROLS</span>
      <span>FROM A NON-U.S. PERSPECTIVE TRAINING</span>
    </h1>
  </section>

  <section class="schedule">
    <div class="schedule-divider"></div>
    <div class="schedule-row" style="top:20px"><span class="schedule-city">BRISBANE</span><span>16 &amp; 17 MARCH</span></div>
    <div class="schedule-row" style="top:53px"><span class="schedule-city">SYDNEY</span><span>18 &amp; 19 MARCH</span></div>
    <div class="schedule-row" style="top:85px"><span class="schedule-city">CANBERRA</span><span>20 &amp; 23 MARCH</span></div>
    <div class="schedule-row" style="top:116px"><span class="schedule-city">MELBOURNE</span><span>24 &amp; 25 MARCH</span></div>
    <div class="schedule-row" style="top:148px"><span class="schedule-city">ADELAIDE</span><span>26 &amp; 27 MARCH</span></div>
  </section>

  <section class="intro">
    <p><strong>U.S. Export Controls</strong> are some of the most complex and stringent in the world. The U.S. Government regulates the transfer of U.S. origin goods and technical data throughout the world, with the intent of preventing unauthorised transfer of technology and know-how. These controls extend world-wide and can impact anyone dealing in U.S. controlled goods or technology.</p>
    <p><strong>This two-day comprehensive course</strong> will give applicants a greater understanding of U.S. Export Controls from a non-U.S. perspective in practical and relevant terms.</p>
  </section>

  <p class="price">$1295.00 AUD per person <small>inc GST</small></p>
  <label class="sme-note"><input class="sme-tick" type="checkbox" name="sme-free">Small to Medium Enterprises FREE OF CHARGE</label>
  <p class="subsidy-note">Subsidised by the Allied Industry Capability Office (AICO)</p>

  <footer class="footer">For more information, please contact NTC on +61 (0)7 5550 0142 or info@northlinetc.com</footer>
</main>
</body>
</html>
```